Special Educational Conference Poster

Looking for a poster that I can use electronically more than anything - to post on Facebook \ social media. Should be bold, eye catching, and within our brand colors.

3rd Annual Young Learners Brightpath Summit
Featuring Dr. Alan Whitford
The Power of Mindsets: Nurturing Motivation, Hope, and Resilience in Children with Special Needs

Friday, May 10, 2019, 9am - 3pm

The Meadowlark School at Pinecrest opens our campus to teachers, parents, and practitioners from the Delaware Valley to learn together on how to support the extraordinary students in our lives. The conference runs from 9am - 3pm and lunch is included. This event is free and open to the public, but registration is required.

Link to registration: https://www.meadowlarkacademy-example.org/admissions/admissions-visit-and-events

```html
<!DOCTYPE html>
<html lang="en">
<head>
<meta charset="utf-8">
<title>3rd Annual Young Learners Brightpath Summit</title>
<link rel="stylesheet" href="https://fonts.googleapis.com/css2?family=Mulish:wght@600;700;800&family=Didact+Gothic&family=Dosis:wght@300;400&family=Nunito:wght@800;900&display=swap">
<style>
  :root {
    --teal: #13a9d6;
    --ink: #111111;
    --white: #ffffff;
    --body-grey: #2a2522;
    --date-red: #e51d35;
    --band-red: #d5132a;
    --band-deep: #a50d1f;
    --sky-top: #e9c3b0;
    --sky-mid: #e3b89c;
    --horizon: #f4dcc0;
    --sand-light: #dca572;
    --sand-deep: #c07c45;
    --shade: rgba(90,50,30,0.38);
  }
  * { box-sizing: border-box; margin: 0; padding: 0; }
  html, body { width: 1200px; height: 720px; overflow: hidden; background: var(--white); }
  .poster {
    position: relative;
    width: 1200px;
    height: 720px;
    overflow: hidden;
    font-family: "Mulish", sans-serif;
  }
  .scene-photo {
    position: absolute;
    inset: 0;
    background:
      radial-gradient(ellipse 360px 150px at 250px 380px, var(--shade), rgba(90,50,30,0) 75%),
      radial-gradient(ellipse 420px 200px at 640px 500px, rgba(255,244,226,0.85), rgba(255,244,226,0) 70%),
      radial-gradient(ellipse 380px 170px at 910px 390px, rgba(255,246,236,0.55), rgba(255,246,236,0) 75%),
      linear-gradient(180deg, var(--sky-top) 0%, var(--sky-mid) 45%, var(--horizon) 70%, var(--sand-light) 80%, var(--sand-deep) 100%);
  }
  .brand-cap {
    position: absolute;
    left: 0; top: 0;
    width: 400px; height: 180px;
  }
  .brand-name {
    position: absolute;
    left: 48px; top: 54px;
    display: flex; align-items: center; gap: 10px;
    color: var(--teal);
    font-weight: 700;
    font-size: 34px;
    letter-spacing: 0.5px;
  }
  .brand-dot {
    width: 18px; height: 18px; border-radius: 50%;
    background: var(--teal);
  }
  .edition {
    position: absolute;
    left: 0; width: 1264px; top: 82px;
    text-align: center;
    color: var(--teal);
    font-weight: 700;
    font-size: 74px;
    line-height: 1;
    letter-spacing: -1px;
  }
  .event-title {
    position: absolute;
    left: 0; width: 1224px; top: 182px;
    text-align: center;
    color: var(--ink);
    font-weight: 800;
    font-size: 46px;
    line-height: 1;
    text-shadow: 0 0 3px var(--white), 0 0 3px var(--white), 0 0 6px var(--white);
  }
  .speaker {
    position: absolute;
    left: 28px; top: 268px;
    color: var(--white);
    font-weight: 700;
    font-size: 24px;
    line-height: 1;
    text-shadow: 1px 1px 2px rgba(30,15,10,0.95), 0 0 6px rgba(30,15,10,0.6);
  }
  .theme {
    position: absolute;
    left: 28px; top: 312px;
    width: 488px;
    color: var(--white);
    font-family: "Didact Gothic", sans-serif;
    font-size: 31px;
    line-height: 40px;
    text-shadow: 1px 1px 2px rgba(30,15,10,0.95), 0 0 6px rgba(30,15,10,0.65);
  }
  .theme span { display: block; text-align: justify; text-align-last: justify; }
  .theme span.last { text-align-last: left; }
  .about {
    position: absolute;
    left: 652px; top: 308px;
    width: 510px;
    color: var(--body-grey);
    font-family: "Dosis", sans-serif;
    font-weight: 400;
    font-size: 19px;
    line-height: 26.6px;
    text-align: justify;
    text-align-last: left;
    text-shadow: 0 0 2px var(--white), 0 0 4px var(--white);
  }
  .bottom-band {
    position: absolute;
    left: 0; bottom: 0;
    width: 1200px; height: 160px;
  }
  .event-date {
    position: absolute;
    left: 0; width: 1228px; top: 579px;
    text-align: center;
    color: var(--date-red);
    font-family: "Nunito", sans-serif;
    font-weight: 900;
    font-size: 39px;
    line-height: 1;
    -webkit-text-stroke: 1px var(--white);
    text-shadow: 0 0 3px var(--white), 0 0 2px var(--white);
  }
  .registration {
    position: absolute;
    left: 34px; top: 664px;
    color: var(--white);
    font-weight: 700;
    font-size: 21px;
    line-height: 1;
    white-space: nowrap;
  }
  .registration .label { margin-right: 9px; }
</style>
</head>
<body>
<main class="poster">
  <div class="scene-photo" role="img" aria-label="Photograph: a young child on a sandy beach at sunset, waving a long flowing orange fabric streamer overhead against a soft hazy sky"></div>

  <svg class="brand-cap" viewBox="0 0 400 180" aria-hidden="true">
    <ellipse cx="150" cy="30" rx="248" ry="146" fill="#ffffff"/>
  </svg>
  <div class="brand-name"><span class="brand-dot"></span>Solvia Pharmacy</div>

  <h1>
    <span class="edition">3rd Annual</span>
    <span class="event-title">Young Learners Brightpath Summit</span>
  </h1>

  <p class="speaker">Featuring Dr. Alan Whitford</p>

  <p class="theme">
    <span>The Power of Mindsets: Nurturing</span>
    <span>Motivation, Hope, and Resilience in</span>
    <span class="last">Children with Special Needs</span>
  </p>

  <p class="about">The Meadowlark School at Pinecrest opens our campus to teachers, parents, and practitioners from the Delaware Valley to learn together on how to support the extraordinary students in our lives. The conference runs from 9am - 3pm and lunch is included. This event is free and open to the public, but registration is required.</p>

  <svg class="bottom-band" viewBox="0 0 1200 160" preserveAspectRatio="none" aria-hidden="true">
    <path d="M0 10 L90 40 L0 70 Z" fill="#e0283b"/>
    <path d="M1200 10 L1110 40 L1200 70 Z" fill="#e0283b"/>
    <path d="M0 40 C200 70 380 90 600 92 C820 90 1000 70 1200 40 L1200 160 L0 160 Z" fill="var(--band-red)"/>
    <path d="M0 95 C220 108 420 116 600 116 C780 116 980 108 1200 95 L1200 160 L0 160 Z" fill="var(--band-deep)"/>
  </svg>

  <p class="event-date">Friday, May 10, 2019, 9am - 3pm</p>

  <p class="registration"><span class="label">Link to registration:</span>https://www.meadowlarkacademy-example.org/admissions/admissions-visit-and-events</p>
</main>
</body>
</html>
```